MS Word Template needed for a company specialized in network and security infrastructures

We need a new MS Word Template. <br/>Our activity is services in IT (network infrastructure and security). We usually use french language. <br/>The template must be nice and beautiful, and easy to use. If possible, try to use as less as possible text zones to simplify redaction tasks. And try to use "native" polices in MS Word. I attached sample documents for example. Please try to use the same colour codes.

Target Market(s)

Consulting in Network and security domain

Industry/Entity Type

It Service

Colors

Designer to choose colors to be used in the design.

Requirements
Must have
• - Nice design
• - Easy to use
• - very professional aspect
Nice to have
• - actual oxa cable partners logo
• - actual colour code

```html
<!DOCTYPE html>
<html lang="fr">
<head>
<meta charset="utf-8">
<title>Oxa Cable Partners – Modèle de document</title>
<link href="https://fonts.googleapis.com/css2?family=Montserrat:wght@400;500;600;700;800;900&family=Open+Sans:wght@400;600;700&display=swap" rel="stylesheet">
<style>
  :root{
    --board:#4a4a4a;
    --navy:#0c2241;
    --navy-deep:#071a33;
    --teal:#00a0b2;
    --teal-dark:#0a7f8f;
    --green:#1f9e78;
    --ink:#111;
    --paper:#fff;
  }
  *{box-sizing:border-box;margin:0;padding:0}
  html,body{width:1200px;height:1123px;overflow:hidden;background:var(--board)}
  body{font-family:"Open Sans",Arial,sans-serif;color:var(--ink);position:relative}
  .page{position:absolute;width:370px;height:528px;background:var(--paper);overflow:hidden}
  .p1{left:22px;top:22px;background:var(--navy)}
  .p2{left:415px;top:22px}
  .p3{left:807px;top:22px}
  .p4{left:22px;top:572px}
  .p5{left:415px;top:572px}
  .p6{left:807px;top:572px}
  .abs{position:absolute}

  /* cover */
  .cover-photo{left:0;top:0;width:370px;height:107px;background:linear-gradient(180deg,#2b2f35 0%,#1a1d22 55%,#30343a 100%)}
  .cover-brand{left:0;top:212px;width:370px;text-align:center;font-family:"Montserrat",sans-serif;font-weight:600;font-size:19px;letter-spacing:1.5px;color:var(--teal)}
  .cover-box{left:33px;top:356px;width:305px;height:118px;background:var(--teal);padding:34px 26px 0 27px;color:#fff;font-family:"Montserrat",sans-serif;font-size:7.6px;line-height:10px;box-shadow:0 3px 8px rgba(0,0,0,.35)}
  .cover-box p+p{margin-top:10px}

  /* table of content */
  .toc-title{left:14px;top:191px;font-family:"Montserrat",sans-serif;font-weight:800;font-size:21.5px;color:#222;letter-spacing:-.2px}
  .toc-body{left:0;top:244px;width:370px;height:284px;background:var(--navy-deep)}
  .toc-band{position:absolute;left:12px;width:350px;height:47px;background:var(--teal)}
  .toc-item{position:absolute;display:flex;align-items:center;height:40px;color:#fff}
  .toc-num{font-family:"Montserrat",sans-serif;font-weight:900;font-size:30px;width:48px;letter-spacing:-1px}
  .toc-rule{width:1.5px;height:24px;background:#fff;margin:0 9px 0 0}
  .toc-label{font-family:"Montserrat",sans-serif;font-weight:500;font-size:7.8px;line-height:10px}

  /* running header & footer */
  .run-head{left:133px;top:30px;font-family:"Montserrat",sans-serif;font-weight:500;font-size:8px;color:#111}
  .run-bar{left:309px;top:24px;width:61px;height:15px;background:var(--teal)}
  .foot-brand{left:22px;display:flex;align-items:center;gap:5px;font-family:"Montserrat",sans-serif;font-weight:600;font-size:8.5px;color:var(--teal);letter-spacing:.4px}
  .foot-dot{width:14px;height:14px;border-radius:50%;background:var(--teal)}
  .foot-note{right:29px;text-align:right;font-family:"Montserrat",sans-serif;font-weight:500;font-size:7.8px;line-height:10px;color:#111}

  .body-text{font-family:"Montserrat",sans-serif;font-size:7.7px;line-height:10px;text-align:justify;color:#111}
  .tile{top:62px;width:99px;height:65px;background:var(--teal)}
  .tech-photo{background:radial-gradient(circle at 50% 55%,#1f5f82 0%,#0f3552 35%,#061827 70%,#02080f 100%)}

  /* quote */
  .quote-box{left:22px;top:62px;width:318px;height:125px;background:var(--teal);color:#fff;padding:8px 12px 0 12px}
  .quote-mark{font-family:"Montserrat",sans-serif;font-weight:900;font-size:34px;line-height:30px;height:22px}
  .quote-text{font-family:"Montserrat",sans-serif;font-weight:500;font-size:7.6px;line-height:10px;text-align:justify}

  /* sites map */
  .map-art{left:132px;top:212px;width:126px;height:226px;background:linear-gradient(160deg,#0c3c4e 0%,#0f6a63 45%,#1e9e78 100%);border-radius:40% 30% 45% 35%}
  .site-icon{width:15px;height:15px;border-radius:50%;border:1px solid #bfe7ec;background:#fff}
  .site-title{font-family:"Open Sans",sans-serif;font-weight:700;font-size:5.4px;line-height:7px;color:var(--teal)}
  .site-cap{font-family:"Open Sans",sans-serif;font-weight:700;font-style:italic;font-size:3.4px;line-height:4px;color:var(--teal)}
  .site-code{font-family:"Open Sans",sans-serif;font-weight:700;font-size:4.8px;color:#111}
  .site-addr{font-family:"Open Sans",sans-serif;font-size:3.6px;line-height:4.6px;color:#222;width:75px}
  .shop-title{font-family:"Open Sans",sans-serif;font-weight:700;font-size:7.6px;color:#111}
  .shop-pill{width:71px;height:19px;border-radius:10px;background:var(--teal);color:#fff;display:flex;align-items:center;padding-left:8px;gap:5px;box-shadow:0 1px 3px rgba(0,0,0,.25)}
  .shop-pill i{display:block;width:11px;height:8px;border:1px solid #fff;border-radius:1px}
  .shop-pill span{font-family:"Open Sans",sans-serif;font-weight:700;font-size:5.4px;line-height:6px}
  .shop-pill small{display:block;font-size:3.8px}
  .leader{stroke:var(--teal);stroke-width:.5;fill:none}
</style>
</head>
<body>

<!-- Cover -->
<section class="page p1">
  <div class="abs cover-photo" role="img" aria-label="Photo d'une salle de serveurs avec icônes réseau en surimpression"></div>
  <div class="abs cover-brand">OXA CABLE PARTNERS</div>
  <div class="abs cover-box">
    <p>Lorem ipsum dolor sit amet, consectetur adipisicing elit, sed do eiusmod tempor incididunt ut labore et dolore magna aliqu</p>
    <p>a. Ut enim ad minim veniam, quis nostrud exercitation ullamco laboris nisi ut aliquip ex ea commodo consequat. Duis aute irure</p>
  </div>
</section>

<!-- Table of content -->
<section class="page p2">
  <h1 class="abs toc-title">TABLE OF CONTENT</h1>
  <div class="abs toc-body">
    <div class="toc-band" style="top:81px"></div>
    <div class="toc-band" style="top:192px;left:14px"></div>

    <div class="toc-item" style="left:32px;top:29px"><span class="toc-num">01</span><span class="toc-rule"></span><span class="toc-label">Lorem ipsum dolor<br>sit amet, consectetur</span></div>
    <div class="toc-item" style="left:210px;top:29px"><span class="toc-num">05</span><span class="toc-rule"></span><span class="toc-label">Lorem ipsum dolor<br>sit amet, consectetur</span></div>

    <div class="toc-item" style="left:32px;top:85px"><span class="toc-num">02</span><span class="toc-rule"></span><span class="toc-label">Lorem ipsum dolor<br>sit amet, consectetur</span></div>
    <div class="toc-item" style="left:210px;top:85px"><span class="toc-num">06</span><span class="toc-rule"></span><span class="toc-label">Lorem ipsum dolor<br>sit amet, consectetur</span></div>

    <div class="toc-item" style="left:32px;top:140px"><span class="toc-num">03</span><span class="toc-rule"></span><span class="toc-label">Lorem ipsum dolor<br>sit amet, consectetur</span></div>
    <div class="toc-item" style="left:210px;top:137px"><span class="toc-num">07</span><span class="toc-rule"></span><span class="toc-label">Lorem ipsum dolor<br>sit amet, consectetur</span></div>

    <div class="toc-item" style="left:32px;top:195px"><span class="toc-num">04</span><span class="toc-rule"></span><span class="toc-label">Lorem ipsum dolor<br>sit amet, consectetur</span></div>
    <div class="toc-item" style="left:210px;top:194px"><span class="toc-num">08</span><span class="toc-rule"></span><span class="toc-label">Lorem ipsum dolor<br>sit amet, consectetur</span></div>
  </div>
</section>

<!-- Three columns page -->
<section class="page p3">
  <div class="abs run-head">Lorem ipsum dolor sit amet, consectetur</div>
  <div class="abs run-bar"></div>
  <div class="abs tile" style="left:22px"></div>
  <div class="abs tile" style="left:133px"></div>
  <div class="abs tile" style="left:245px"></div>
  <p class="abs body-text" style="left:22px;top:140px;width:95px">Lorem ipsum dolor sit amet, consectetur adipisicing elit, sed do eiusmod tempor incididunt ut labore et dolore magna aliqua. Ut enim ad minim veniam, quis nostrud exercitation ullamco laboris nisi ut aliquip ex ea commodo consequat. Duis aute irure dolor in</p>
  <p class="abs body-text" style="left:133px;top:140px;width:99px">Lorem ipsum dolor sit amet, consectetur adipisicing elit, sed do eiusmod tempor incididunt ut labore et dolore magna aliqua. Ut enim ad minim veniam, quis nostrud exercitation ullamco laboris nisi ut aliquip ex ea commodo consequat. Duis aute irure dolor in reprehenderit in</p>
  <p class="abs body-text" style="left:245px;top:140px;width:95px">Lorem ipsum dolor sit amet, consectetur adipisicing elit, sed do eiusmod tempor incididunt ut labore et dolore magna aliqua. Ut enim ad minim veniam, quis nostrud exercitation ullamco laboris nisi ut aliquip ex ea commodo consequat. Duis aute irure dolor in</p>
  <div class="abs tech-photo" style="left:22px;top:276px;width:319px;height:160px" role="img" aria-label="Visuel technologique bleu avec cercles de données"></div>
  <div class="abs foot-brand" style="top:494px"><span class="foot-dot"></span>OXA CABLE PARTNERS</div>
  <div class="abs foot-note" style="top:489px">Lorem ipsum dolor sit<br>amet, consectetur</div>
</section>

<!-- Chart page -->
<section class="page p4">
  <div class="abs run-head">Lorem ipsum dolor sit amet, consectetur</div>
  <div class="abs run-bar"></div>
  <svg class="abs" style="left:0;top:0" width="370" height="212" viewBox="0 0 370 212" role="img" aria-label="Histogramme du chiffre d'affaires en k€ de 2015 à 2019">
    <defs>
      <linearGradient id="barFill" x1="0" y1="0" x2="0" y2="1">
        <stop offset="0" stop-color="#1f6f8a"/>
        <stop offset="1" stop-color="#2fb07e"/>
      </linearGradient>
    </defs>
    <g stroke="#d9d9d9" stroke-width=".6">
      <line x1="61" y1="66" x2="325" y2="66"/><line x1="61" y1="82.5" x2="325" y2="82.5"/>
      <line x1="61" y1="99" x2="325" y2="99"/><line x1="61" y1="115.5" x2="325" y2="115.5"/>
      <line x1="61" y1="132" x2="325" y2="132"/><line x1="61" y1="148.5" x2="325" y2="148.5"/>
      <line x1="61" y1="165" x2="325" y2="165"/><line x1="61" y1="62" x2="61" y2="165"/>
    </g>
    <g font-family="Open Sans, sans-serif" font-size="11" fill="#111" text-anchor="end">
      <text x="50" y="70">1,200</text><text x="50" y="86.5">1,000</text><text x="50" y="103">800</text>
      <text x="50" y="119.5">600</text><text x="50" y="136">400</text><text x="50" y="152.5">200</text><text x="50" y="169">0</text>
    </g>
    <g fill="url(#barFill)">
      <rect x="78" y="142.7" width="16" height="22.3"/>
      <rect x="131" y="130.4" width="16" height="34.6"/>
      <rect x="184" y="116.3" width="16" height="48.7"/>
      <rect x="237" y="94.9" width="16" height="70.1"/>
      <rect x="289" y="66.8" width="16" height="98.2"/>
    </g>
    <g font-family="Open Sans, sans-serif" font-size="11" fill="#111" text-anchor="middle">
      <text x="86" y="183">2015</text><text x="139" y="183">2016</text><text x="192" y="183">2017</text>
      <text x="245" y="183">2018</text><text x="297" y="183">2019</text>
    </g>
    <rect x="151" y="198" width="5" height="5" fill="#2a9a80"/>
    <text x="159" y="204" font-family="Open Sans, sans-serif" font-size="10.5" fill="#111">CA en k€</text>
  </svg>
  <p class="abs body-text" style="left:18px;top:213px;width:158px">Lorem ipsum dolor sit amet, consectetur adipiscing elit, sed do eiusmod tempor incididunt ut labore et dolore magna aliqua. Quis ipsum suspendisse ultrices gravida. Risus commodo viverra maecenas accumsan lacus vel facilisis. Lorem ipsum dolor sit amet, consectetur adipiscing elit, sed do eiusmod tempor incididunt ut labore et dolore magna aliqua. Ut enim ad minim veniam, quis nostrud exercitation ullamco laboris nisi ut aliquip</p>
  <p class="abs body-text" style="left:191px;top:213px;width:157px">ex ea commodo consequat. Duis aute irure dolor in reprehenderit in voluptate velit esse cillum dolore eu fugiat nulla pariatur. Excepteur sint occaecat cupidatat non proident, sunt in culpa qui officia deserunt mollit anim id est laborum. Sed ut perspiciatis unde omnis iste natus error sit voluptatem accusantium doloremque laudantium, totam rem aperiam, eaque ipsa quae ab illo inventore veritatis et quasi architecto beatae vitae dicta sunt</p>
  <div class="abs tech-photo" style="left:18px;top:331px;width:329px;height:134px" role="img" aria-label="Visuel technologique bleu avec cercles de données"></div>
  <div class="abs foot-brand" style="top:503px;left:24px"><span class="foot-dot"></span>OXA CABLE PARTNERS</div>
  <div class="abs foot-note" style="top:498px;right:27px">Lorem ipsum dolor sit<br>amet, consectetur</div>
</section>

<!-- Sites pages -->
<section class="page p5">
  <div class="abs run-head" style="left:134px">Lorem ipsum dolor sit amet, consectetur</div>
  <div class="abs run-bar"></div>
  <div class="abs quote-box">
    <div class="quote-mark">“</div>
    <p class="quote-text">Lorem ipsum dolor sit amet, consectetur adipisicing elit, sed do eiusmod tempor incididunt ut labore et dolore magna aliqua. Ut enim ad minim veniam, quis nostrud exercitation ullamco laboris nisi ut aliquip ex ea commodo consequat. Duis aute irure dolor in reprehenderit in voluptate velit esse cillum dolore eu fugiat nulla pariatur. Excepteur sint occaecat cupidatat non proident, sunt in culpa qui officia deserunt mollit anim id est laborum. Sed ut perspiciatis unde omnis iste natus error sit voluptatem accusantium doloremque laudantium, totam rem aperiam, eaque ipsa quae ab illo inventore</p>
  </div>
  <div class="abs map-art" role="img" aria-label="Carte du Royaume-Uni, de la Belgique et de la France avec les sites"></div>
  <svg class="abs" style="left:0;top:0" width="370" height="528" viewBox="0 0 370 528">
    <polyline class="leader" points="230,258 200,258 200,285"/>
    <polyline class="leader" points="230,264 200,264"/>
    <polyline class="leader" points="230,319 205,319 200,314"/>
    <polyline class="leader" points="108,325 120,325 120,310 178,310"/>
    <polyline class="leader" points="108,339 120,339"/>
    <polyline class="leader" points="108,353 130,353 130,340 178,340"/>
    <polyline class="leader" points="126,413 182,413 182,335"/>
    <polyline class="leader" points="108,426 185,426 185,335"/>
    <polyline class="leader" points="248,372 238,372 238,330 220,330"/>
    <polyline class="leader" points="248,398 232,398 232,345"/>
  </svg>

  <div class="abs site-icon" style="left:261px;top:214px"></div>
  <div class="abs site-title" style="left:277px;top:216px">Sites Centraux<br>en Angleterre</div>
  <div class="abs site-cap" style="left:248px;top:237px">Nom du<br>site</div>
  <div class="abs site-cap" style="left:277px;top:239px">Adresse Postale</div>
  <div class="abs site-code" style="left:250px;top:249px">BGY</div>
  <div class="abs site-addr" style="left:277px;top:249px">12 Harlow Mill Lane, Brackton BX4 2LP, Royaume-Uni</div>
  <div class="abs site-code" style="left:250px;top:263px">STN</div>
  <div class="abs site-addr" style="left:277px;top:263px">7 Ferncliff Road, Ashby Vale AV2 9TT, Royaume-Uni</div>

  <div class="abs site-icon" style="left:261px;top:281px"></div>
  <div class="abs site-title" style="left:277px;top:283px">Sites Centraux<br>en Belgique</div>
  <div class="abs site-cap" style="left:248px;top:304px">Nom du<br>site</div>
  <div class="abs site-cap" style="left:277px;top:306px">Adresse Postale</div>
  <div class="abs site-code" style="left:250px;top:315px">DOT</div>
  <div class="abs site-addr" style="left:277px;top:315px">Rue des Tilleuls 41, 7700 Lormont, Belgique</div>

  <div class="abs site-icon" style="left:31px;top:285px"></div>
  <div class="abs site-title" style="left:55px;top:287px">Sites Centraux<br>en France</div>
  <div class="abs site-cap" style="left:27px;top:308px">Nom du<br>site</div>
  <div class="abs site-cap" style="left:55px;top:310px">Adresse Postale</div>
  <div class="abs site-code" style="left:35px;top:319px">DA</div>
  <div class="abs site-addr" style="left:55px;top:321px">88 Boulevard Marceline 59100 Vernay</div>
  <div class="abs site-code" style="left:32px;top:333px">FAC</div>
  <div class="abs site-addr" style="left:55px;top:334px">14 allée des Saules 59170 Vernay</div>
  <div class="abs site-code" style="left:28px;top:347px">CLEM</div>
  <div class="abs site-addr" style="left:55px;top:348px">31 rue Clément Ader 59510 Hautmont</div>

  <div class="abs site-icon" style="left:31px;top:378px"></div>
  <div class="abs site-title" style="left:55px;top:383px">Data Centers</div>
  <div class="abs site-cap" style="left:27px;top:398px">Nom du<br>site</div>
  <div class="abs site-cap" style="left:55px;top:400px">Adresse Postale</div>
  <div class="abs site-code" style="left:23px;top:409px">CACOM</div>
  <div class="abs site-addr" style="left:55px;top:410px">Nexium PX2, 9 rue Lavoisier, 93200 Saint-Orly</div>
  <div class="abs site-code" style="left:28px;top:423px">ARVO</div>
  <div class="abs site-addr" style="left:55px;top:424px">62 avenue des Lilas 93300 Belvaux</div>

  <div class="abs shop-title" style="left:252px;top:345px">Magasins Velmont</div>
  <div class="abs shop-pill" style="left:253px;top:362px"><i></i><span>Belgique<small>56 magasins</small></span></div>
  <div class="abs shop-pill" style="left:253px;top:388px"><i></i><span>France<small>96 magasins</small></span></div>

  <div class="abs foot-brand" style="top:497px;left:30px"><span class="foot-dot"></span>OXA CABLE PARTNERS</div>
  <div class="abs foot-note" style="top:493px;right:22px">Lorem ipsum dolor sit<br>amet, consectetur</div>
</section>

<section class="page p6">
  <div class="abs run-head" style="left:134px">Lorem ipsum dolor sit amet, consectetur</div>
  <div class="abs run-bar"></div>
  <div class="abs quote-box">
    <div class="quote-mark">“</div>
    <p class="quote-text">Lorem ipsum dolor sit amet, consectetur adipisicing elit, sed do eiusmod tempor incididunt ut labore et dolore magna aliqua. Ut enim ad minim veniam, quis nostrud exercitation ullamco laboris nisi ut aliquip ex ea commodo consequat. Duis aute irure dolor in reprehenderit in voluptate velit esse cillum dolore eu fugiat nulla pariatur. Excepteur sint occaecat cupidatat non proident, sunt in culpa qui officia deserunt mollit anim id est laborum. Sed ut perspiciatis unde omnis iste natus error sit voluptatem accusantium doloremque laudantium, totam rem aperiam, eaque ipsa quae ab illo inventore</p>
  </div>
  <div class="abs map-art" role="img" aria-label="Carte du Royaume-Uni, de la Belgique et de la France avec les sites"></div>
  <svg class="abs" style="left:0;top:0" width="370" height="528" viewBox="0 0 370 528">
    <polyline class="leader" points="230,258 200,258 200,285"/>
    <polyline class="leader" points="230,264 200,264"/>
    <polyline class="leader" points="230,319 205,319 200,314"/>
    <polyline class="leader" points="108,325 120,325 120,310 178,310"/>
    <polyline class="leader" points="108,339 120,339"/>
    <polyline class="leader" points="108,353 130,353 130,340 178,340"/>
    <polyline class="leader" points="126,413 182,413 182,335"/>
    <polyline class="leader" points="108,426 185,426 185,335"/>
    <polyline class="leader" points="248,372 238,372 238,330 220,330"/>
    <polyline class="leader" points="248,398 232,398 232,345"/>
  </svg>

  <div class="abs site-icon" style="left:261px;top:214px"></div>
  <div class="abs site-title" style="left:277px;top:216px">Sites Centraux<br>en Angleterre</div>
  <div class="abs site-cap" style="left:248px;top:237px">Nom du<br>site</div>
  <div class="abs site-cap" style="left:277px;top:239px">Adresse Postale</div>
  <div class="abs site-code" style="left:250px;top:249px">BGY</div>
  <div class="abs site-addr" style="left:277px;top:249px">12 Harlow Mill Lane, Brackton BX4 2LP, Royaume-Uni</div>
  <div class="abs site-code" style="left:250px;top:263px">STN</div>
  <div class="abs site-addr" style="left:277px;top:263px">7 Ferncliff Road, Ashby Vale AV2 9TT, Royaume-Uni</div>

  <div class="abs site-icon" style="left:261px;top:281px"></div>
  <div class="abs site-title" style="left:277px;top:283px">Sites Centraux<br>en Belgique</div>
  <div class="abs site-cap" style="left:248px;top:304px">Nom du<br>site</div>
  <div class="abs site-cap" style="left:277px;top:306px">Adresse Postale</div>
  <div class="abs site-code" style="left:250px;top:315px">DOT</div>
  <div class="abs site-addr" style="left:277px;top:315px">Rue des Tilleuls 41, 7700 Lormont, Belgique</div>

  <div class="abs site-icon" style="left:31px;top:285px"></div>
  <div class="abs site-title" style="left:55px;top:287px">Sites Centraux<br>en France</div>
  <div class="abs site-cap" style="left:27px;top:308px">Nom du<br>site</div>
  <div class="abs site-cap" style="left:55px;top:310px">Adresse Postale</div>
  <div class="abs site-code" style="left:35px;top:319px">DA</div>
  <div class="abs site-addr" style="left:55px;top:321px">88 Boulevard Marceline 59100 Vernay</div>
  <div class="abs site-code" style="left:32px;top:333px">FAC</div>
  <div class="abs site-addr" style="left:55px;top:334px">14 allée des Saules 59170 Vernay</div>
  <div class="abs site-code" style="left:28px;top:347px">CLEM</div>
  <div class="abs site-addr" style="left:55px;top:348px">31 rue Clément Ader 59510 Hautmont</div>

  <div class="abs site-icon" style="left:31px;top:378px"></div>
  <div class="abs site-title" style="left:55px;top:383px">Data Centers</div>
  <div class="abs site-cap" style="left:27px;top:398px">Nom du<br>site</div>
  <div class="abs site-cap" style="left:55px;top:400px">Adresse Postale</div>
  <div class="abs site-code" style="left:23px;top:409px">CACOM</div>
  <div class="abs site-addr" style="left:55px;top:410px">Nexium PX2, 9 rue Lavoisier, 93200 Saint-Orly</div>
  <div class="abs site-code" style="left:28px;top:423px">ARVO</div>
  <div class="abs site-addr" style="left:55px;top:424px">62 avenue des Lilas 93300 Belvaux</div>

  <div class="abs shop-title" style="left:252px;top:345px">Magasins Velmont</div>
  <div class="abs shop-pill" style="left:253px;top:362px"><i></i><span>Belgique<small>56 magasins</small></span></div>
  <div class="abs shop-pill" style="left:253px;top:388px"><i></i><span>France<small>96 magasins</small></span></div>

  <div class="abs foot-brand" style="top:497px;left:30px"><span class="foot-dot"></span>OXA CABLE PARTNERS</div>
  <div class="abs foot-note" style="top:493px;right:22px">Lorem ipsum dolor sit<br>amet, consectetur</div>
</section>

</body>
</html>
```